Copperfinch Roofing LLC introduction postcard design

I am looking to get designs for post cards I will be sending out to Homeowners, contractors and Management companies introducing our services, this card will be one sided an area to add a mailing sticker the card will be 4.2x5.5 inches you can get some ideas from www.copperfinchroofing.example

```html
<!DOCTYPE html>
<html lang="en">
<head>
<meta charset="utf-8">
<title>Copperfinch Roofing LLC – Postcard</title>
<link rel="stylesheet" href="https://fonts.googleapis.com/css2?family=Montserrat:wght@400;500;600;700;800&family=Oswald:wght@500;600&display=swap">
<style>
:root{
  --bg:#cfcfcf;
  --ink:#282a3b;
  --navy:#1b4a6b;
  --copper:#c48a57;
  --white:#ffffff;
  --text:#1f2230;
  --stamp:#c8c8c8;
}
*{margin:0;padding:0;box-sizing:border-box}
html,body{width:768px;height:1200px;overflow:hidden;background:var(--bg);font-family:'Montserrat',sans-serif;color:var(--text)}
.card{position:absolute;left:71px;width:626px;height:478px;background:var(--white);overflow:hidden}
.card--front{top:83px}
.card--back{top:639px}
.abs{position:absolute}
.nowrap{white-space:nowrap}
.brand{display:flex;align-items:center;gap:6px;font-family:'Oswald',sans-serif;font-weight:600;color:var(--ink);line-height:1.05}
.brand__dot{width:18px;height:18px;border-radius:50%;background:var(--copper);flex:none}
.photo{position:absolute;background:linear-gradient(160deg,#9fb9d2,#5d6c7c 60%,#3d4652)}
.thumb{position:absolute;border:2px solid var(--white);border-radius:8px;overflow:hidden}
.headline{left:30px;top:150px;color:var(--white)}
.headline__small{font-family:'Oswald',sans-serif;font-weight:600;font-size:25px;line-height:30px}
.headline__big{font-weight:800;font-size:35px;line-height:32px;color:var(--copper);letter-spacing:-.5px}
.pills{left:30px;top:249px;display:flex;gap:5px;font-family:'Oswald',sans-serif;font-weight:500;font-size:11.5px;color:var(--white);align-items:center;white-space:nowrap}
.pills span{display:flex;align-items:center;gap:3px}
.intro{left:30px;top:289px;width:244px;font-size:9.8px;line-height:12.3px;font-weight:500;letter-spacing:-.1px}
.vrule{position:absolute;width:1px;background:#9aa0aa}
.services{left:293px;top:308px;display:grid;grid-template-columns:148px 170px;row-gap:4px;font-size:10px;font-weight:500;white-space:nowrap}
.services li{list-style:none;display:flex;align-items:center;gap:4px;height:13px}
.band{position:absolute;left:0;right:0;background:var(--navy);color:var(--white)}
.trusted{left:30px;top:7px;font-weight:700;font-size:13.5px}
.tag{left:30px;top:24px;width:108px;height:26px;background:var(--copper);font-family:'Oswald',sans-serif;font-weight:500;font-size:8px;line-height:10px;color:var(--ink);padding:3px 4px;white-space:nowrap;letter-spacing:-.1px}
.guarantee{left:141px;top:24px;width:128px;height:26px;background:var(--white);color:var(--navy);font-weight:800;font-size:16px;display:flex;align-items:center;justify-content:center;letter-spacing:.3px;white-space:nowrap}
.address{left:30px;top:55px;font-size:10px;font-weight:500;display:flex;gap:5px;align-items:center;white-space:nowrap}
.contact{left:293px;top:8px;font-size:10.5px;font-weight:500;white-space:nowrap}
.contact div{display:flex;align-items:center;gap:4px;height:15.5px}
.contact b{font-weight:700}
.why{left:31px;top:30px;display:flex;gap:2px;font-weight:700;font-size:9.6px;white-space:nowrap}
.why span{height:20px;display:flex;align-items:center;padding:0 4px}
.why__a{background:var(--copper);color:var(--white);width:107px}
.why__b{background:var(--white);color:var(--ink);width:111px}
.para{left:31px;color:var(--white);font-size:9.8px;line-height:12.3px;font-weight:500;letter-spacing:-.1px}
.pill{position:absolute;left:31px;height:15px;border-radius:8px;background:var(--navy);color:var(--white);font-size:9px;font-weight:600;display:flex;align-items:center;gap:4px;padding:0 10px 0 5px;white-space:nowrap}
.hrule{position:absolute;left:31px;width:253px;height:1px;background:#6b7080}
.addr-line{position:absolute;left:403px;width:193px;height:1px;background:#555}
.stamp{left:520px;top:30px;width:76px;height:76px;background:var(--stamp)}
</style>
</head>
<body>

<section class="card card--front">
  <div class="brand abs" style="left:30px;top:52px;font-size:20px">
    <span class="brand__dot"></span><span>COPPERFINCH<br>ROOFING LLC</span>
  </div>

  <svg class="abs" style="left:0;top:0" width="626" height="278" viewBox="0 0 626 278">
    <polygon points="0,145 222,145 278,278 0,278" fill="#282a3b"/>
    <polygon points="256,0 275,0 223,101 214,101" fill="#c48a57"/>
  </svg>
  <div class="photo" role="img" aria-label="Roofer in safety gear working on a metal standing-seam roof under a blue sky"
       style="left:0;top:0;width:626px;height:278px;clip-path:polygon(276px 0,626px 0,626px 278px,278px 278px,214px 124px)"></div>

  <div class="thumb" role="img" aria-label="Worker repairing a red tile roof next to a brick chimney" style="left:292px;top:205px;width:99px;height:90px;background:linear-gradient(150deg,#6d9a55,#b0533d 70%)"></div>
  <div class="thumb" role="img" aria-label="Aerial view of a home with a grey metal roof" style="left:395px;top:205px;width:99px;height:90px;background:linear-gradient(150deg,#5f8a49,#5e6f80 60%,#8f969a)"></div>
  <div class="thumb" role="img" aria-label="Roofer with a nail gun fastening metal roof panels" style="left:499px;top:205px;width:98px;height:90px;background:linear-gradient(150deg,#9fbcd8,#c3b896 55%,#6b7683)"></div>

  <div class="headline abs">
    <div class="headline__small">Protect what</div>
    <div class="headline__big">MATTERS</div>
    <div class="headline__big" style="display:flex;align-items:center;gap:12px">MOST
      <svg width="29" height="27" viewBox="0 0 29 27"><rect x="0" y="0" width="13" height="12" fill="#fff"/><rect x="16" y="0" width="13" height="12" fill="#fff"/><rect x="0" y="15" width="13" height="12" fill="#fff"/><rect x="16" y="15" width="13" height="12" fill="#fff"/></svg>
    </div>
  </div>

  <div class="pills abs">
    <span><svg width="15" height="17" viewBox="0 0 15 17"><path d="M7.5 1 14 3.5v5c0 4-3 6.5-6.5 7.5C4 15 1 12.5 1 8.5v-5Z" fill="#1b4a6b" stroke="#5aa0d8" stroke-width="1.2"/></svg>YOUR ROOF</span>
    <span><svg width="15" height="17" viewBox="0 0 15 17"><path d="M7.5 1 14 3.5v5c0 4-3 6.5-6.5 7.5C4 15 1 12.5 1 8.5v-5Z" fill="#1b4a6b" stroke="#5aa0d8" stroke-width="1.2"/></svg>YOUR HOME</span>
    <span><svg width="15" height="17" viewBox="0 0 15 17"><path d="M7.5 1 14 3.5v5c0 4-3 6.5-6.5 7.5C4 15 1 12.5 1 8.5v-5Z" fill="#1b4a6b" stroke="#5aa0d8" stroke-width="1.2"/></svg>YOUR INVESTMENT</span>
  </div>

  <p class="intro abs">At Copperfinch Roofing, we deliver top-quality roofing solutions built to withstand coastal weather and time. Whether you’re a homeowner, contractor, or property manager, our team provides reliable craftsmanship, honest communication, &amp; long-lasting results every single time</p>

  <div class="vrule" style="left:282px;top:290px;height:85px"></div>

  <ul class="services abs">
    <li><svg width="10" height="10" viewBox="0 0 10 10"><circle cx="5" cy="5" r="4.2" fill="none" stroke="#c48a57" stroke-width="1.1"/><path d="M3 5.2 4.5 6.7 8.5 2.5" fill="none" stroke="#c48a57" stroke-width="1.3"/></svg>Roof Replacement</li>
    <li><svg width="10" height="10" viewBox="0 0 10 10"><circle cx="5" cy="5" r="4.2" fill="none" stroke="#c48a57" stroke-width="1.1"/><path d="M3 5.2 4.5 6.7 8.5 2.5" fill="none" stroke="#c48a57" stroke-width="1.3"/></svg>Storm Damage Services</li>
    <li><svg width="10" height="10" viewBox="0 0 10 10"><circle cx="5" cy="5" r="4.2" fill="none" stroke="#c48a57" stroke-width="1.1"/><path d="M3 5.2 4.5 6.7 8.5 2.5" fill="none" stroke="#c48a57" stroke-width="1.3"/></svg>Roof Repairs</li>
    <li><svg width="10" height="10" viewBox="0 0 10 10"><circle cx="5" cy="5" r="4.2" fill="none" stroke="#c48a57" stroke-width="1.1"/><path d="M3 5.2 4.5 6.7 8.5 2.5" fill="none" stroke="#c48a57" stroke-width="1.3"/></svg>Emergency Services</li>
    <li><svg width="10" height="10" viewBox="0 0 10 10"><circle cx="5" cy="5" r="4.2" fill="none" stroke="#c48a57" stroke-width="1.1"/><path d="M3 5.2 4.5 6.7 8.5 2.5" fill="none" stroke="#c48a57" stroke-width="1.3"/></svg>Roof Inspection</li>
    <li><svg width="10" height="10" viewBox="0 0 10 10"><circle cx="5" cy="5" r="4.2" fill="none" stroke="#c48a57" stroke-width="1.1"/><path d="M3 5.2 4.5 6.7 8.5 2.5" fill="none" stroke="#c48a57" stroke-width="1.3"/></svg>Commercial Roofing</li>
    <li><svg width="10" height="10" viewBox="0 0 10 10"><circle cx="5" cy="5" r="4.2" fill="none" stroke="#c48a57" stroke-width="1.1"/><path d="M3 5.2 4.5 6.7 8.5 2.5" fill="none" stroke="#c48a57" stroke-width="1.3"/></svg>Roof Tune-Up Services</li>
    <li><svg width="10" height="10" viewBox="0 0 10 10"><circle cx="5" cy="5" r="4.2" fill="none" stroke="#c48a57" stroke-width="1.1"/><path d="M3 5.2 4.5 6.7 8.5 2.5" fill="none" stroke="#c48a57" stroke-width="1.3"/></svg>Roof Maintenance Program</li>
  </ul>

  <div class="band" style="top:384px;height:94px">
    <div class="trusted abs">Your Trusted</div>
    <div class="tag abs">ROOFING EXPERTS IN PALM<br>HAVEN, FLORIDABUILT TO LAST</div>
    <div class="guarantee abs">GUARANTEED</div>
    <div class="address abs">
      <svg width="12" height="12" viewBox="0 0 12 12"><circle cx="6" cy="6" r="6" fill="#c48a57"/><path d="M6 2.5a2 2 0 0 1 2 2c0 1.5-2 4-2 4s-2-2.5-2-4a2 2 0 0 1 2-2Z" fill="#1b4a6b"/></svg>
      418 Harbor Light Rd, Palm Haven FL 34900
    </div>
    <div class="vrule" style="left:282px;top:12px;height:64px;background:#c9d3dc"></div>
    <div class="contact abs">
      <div><b style="font-size:11.5px">Call Us</b></div>
      <div>
        <svg width="11" height="11" viewBox="0 0 11 11"><circle cx="5.5" cy="5.5" r="5.5" fill="#c48a57"/><path d="M3.5 3c.5 2 2 3.8 4 4.5l.8-.9-1.2-.7-.5.5c-.8-.4-1.5-1.1-1.9-1.9l.5-.5L4.5 2.8Z" fill="#1b4a6b"/></svg>
        (555) 014-2380&nbsp;&nbsp;&nbsp;
        <svg width="11" height="11" viewBox="0 0 11 11"><circle cx="5.5" cy="5.5" r="5.5" fill="#c48a57"/><rect x="2.8" y="3.6" width="5.4" height="3.8" fill="none" stroke="#1b4a6b" stroke-width=".9"/><path d="M2.8 3.6 5.5 5.8 8.2 3.6" fill="none" stroke="#1b4a6b" stroke-width=".9"/></svg>
        hello@copperfinchroofing.example
      </div>
      <div>
        <svg width="11" height="11" viewBox="0 0 11 11"><circle cx="5.5" cy="5.5" r="5.5" fill="#c48a57"/><circle cx="5.5" cy="5.5" r="3" fill="none" stroke="#1b4a6b" stroke-width=".9"/><path d="M2.5 5.5h6M5.5 2.5v6" stroke="#1b4a6b" stroke-width=".8"/></svg>
        www.copperfinchroofing.example
      </div>
      <div><b>Follows us on</b>&nbsp;<span style="width:10px;height:10px;border-radius:50%;background:#3b7bd6;display:inline-block"></span>@Copperfinch-Roofing-LLC</div>
    </div>
  </div>
</section>

<section class="card card--back">
  <svg class="abs" style="left:0;top:0" width="626" height="370" viewBox="0 0 626 370">
    <polygon points="0,0 244,0 332,271 308,370 0,370" fill="#282a3b"/>
    <polygon points="248,6 256,6 342,271 317,370 309,370 334,271" fill="#c48a57"/>
  </svg>

  <div class="why abs"><span class="why__a">Why Choose Us for</span><span class="why__b">Roofing Services?</span></div>
  <p class="para abs" style="top:55px;width:226px">Those searching for roofing repair contractors Palm Haven can select us. We are the top choice for roofing services, thanks to our quality services and ability to deliver great customer experiences.</p>

  <div class="pill" style="top:128px"><svg width="10" height="10" viewBox="0 0 10 10"><circle cx="5" cy="5" r="4.2" fill="none" stroke="#c48a57" stroke-width="1.1"/><path d="M3 5.2 4.5 6.7 8.5 2.5" fill="none" stroke="#c48a57" stroke-width="1.3"/></svg>Fully Licensedand Insured</div>
  <p class="para abs" style="top:149px;width:226px">We are fully licensed and insured, so if an accident takes place during the process, you can still enjoy peace of mind.</p>
  <div class="hrule" style="top:201px"></div>

  <div class="pill" style="top:216px;font-size:10px"><svg width="10" height="10" viewBox="0 0 10 10"><circle cx="5" cy="5" r="4.2" fill="none" stroke="#c48a57" stroke-width="1.1"/><path d="M3 5.2 4.5 6.7 8.5 2.5" fill="none" stroke="#c48a57" stroke-width="1.3"/></svg>Experts in Roofing Services</div>
  <p class="para abs" style="top:239px;width:236px">We are local experts for roofing services, so you can definitely trust us.</p>
  <div class="hrule" style="top:277px"></div>

  <div class="pill" style="top:293px;left:30px;font-size:10px"><svg width="10" height="10" viewBox="0 0 10 10"><circle cx="5" cy="5" r="4.2" fill="none" stroke="#c48a57" stroke-width="1.1"/><path d="M3 5.2 4.5 6.7 8.5 2.5" fill="none" stroke="#c48a57" stroke-width="1.3"/></svg>Fast, Reliable, &amp; Transparent Services</div>
  <p class="para abs" style="top:318px;width:268px">Even if you are searching for emergency roof repair Palm Haven, we are here to help with fast, reliable, and transparent services.</p>

  <div class="brand abs" style="left:399px;top:55px;font-size:15px">
    <span class="brand__dot" style="width:14px;height:14px"></span><span>COPPERFINCH<br>ROOFING LLC</span>
  </div>
  <div class="stamp abs"></div>
  <div class="addr-line" style="top:196px"></div>
  <div class="addr-line" style="top:226px"></div>
  <div class="addr-line" style="top:255px"></div>
  <div class="addr-line" style="top:286px"></div>

  <div class="band" style="top:371px;height:107px">
    <div class="abs" role="img" aria-label="Aerial view of a home with a grey metal roof and pool" style="left:31px;top:12px;width:130px;height:63px;border:1px solid #fff;background:linear-gradient(135deg,#7f8d6a,#b9c0c6 50%,#6aa8b8)"></div>
    <div class="abs" role="img" aria-label="Aerial view of waterfront homes with white roofs" style="left:176px;top:12px;width:130px;height:63px;border:1px solid #fff;background:linear-gradient(170deg,#4f8fa8,#d7dde0 45%,#5d7c52)"></div>
    <div class="abs" role="img" aria-label="Aerial view of a white-roofed home among trees" style="left:321px;top:12px;width:130px;height:63px;border:1px solid #fff;background:linear-gradient(135deg,#4e7a3f,#e6e9ea 50%,#3f6a36)"></div>
    <div class="abs" role="img" aria-label="Aerial view of a large home with a bronze metal roof" style="left:466px;top:12px;width:130px;height:63px;border:1px solid #fff;background:linear-gradient(135deg,#4d7342,#9a8a76 50%,#56753f)"></div>
  </div>
</section>

</body>
</html>
```